BUSINESS book cover

Publishing a book for a specific industry and hope to customize it for different industries in the future. So, design needs to be flexible. I want BRIGHT (possibly orange) cover with large words for title...really do not need illustration. Just the subtitle will change for future editions. Book is going to be 5.25" x 8"

Sorry for any confusion. The title of the book is: "Where Stories Bend Sideways..." The subtitle is: A Comprehensive Member Expderience Guide for Today's Club Management Professional

```html
<!DOCTYPE html>
<html lang="en">
<head>
<meta charset="utf-8">
<title>Where Stories Bend Sideways... — Book Cover Spread</title>
<link rel="stylesheet" href="https://fonts.googleapis.com/css2?family=League+Spartan:wght@700&family=Open+Sans:ital,wdth,wght@0,75..100,400..700;1,75..100,400..700&family=Cinzel:wght@400&family=Tenor+Sans&display=swap">
<style>
  :root {
    --cover-orange: #f6a41d;
    --cover-orange-light: #fbb433;
    --cover-orange-deep: #e8901a;
    --ink: #1f2a33;
    --ghost-title: rgba(150, 90, 10, 0.45);
    --portrait-light: #d9d9d9;
    --portrait-dark: #6c6c6c;
  }
  * { box-sizing: border-box; margin: 0; padding: 0; }
  html, body { width: 1200px; height: 852px; overflow: hidden; }
  body { background: var(--cover-orange); }

  .cover-spread {
    position: relative;
    width: 1200px;
    height: 852px;
    overflow: hidden;
    background:
      radial-gradient(ellipse at 70% 35%, var(--cover-orange-light) 0%, transparent 60%),
      radial-gradient(ellipse at 15% 80%, var(--cover-orange-deep) 0%, transparent 55%),
      var(--cover-orange);
    color: var(--ink);
  }

  .graphic-layer {
    position: absolute;
    inset: 0;
    width: 1200px;
    height: 852px;
  }
  .ghost-title { font-family: "League Spartan", sans-serif; font-weight: 700; font-size: 60px; fill: var(--ghost-title); }
  .spine-title, .spine-author { font-family: "League Spartan", sans-serif; font-weight: 700; font-size: 33px; fill: var(--ink); }
  .front-title { font-family: "League Spartan", sans-serif; font-weight: 700; fill: var(--ink); }
  .front-author { font-family: "Tenor Sans", sans-serif; font-size: 46px; fill: var(--ink); }

  /* Back cover */
  .back-cover {
    position: absolute;
    left: 76px;
    top: 98px;
    width: 442px;
  }
  .back-headline {
    font-family: "Open Sans", sans-serif;
    font-weight: 600;
    font-size: 17.5px;
    line-height: 1.1;
    text-align: center;
    margin-bottom: 12px;
  }
  .back-headline em { font-style: italic; }
  .back-blurb {
    font-family: "Open Sans", sans-serif;
    font-weight: 600;
    font-size: 13.6px;
    line-height: 17.4px;
    text-align: justify;
    margin-bottom: 14px;
  }
  .author-portrait {
    position: absolute;
    left: 75px;
    top: 524px;
    width: 235px;
    height: 156px;
    background: linear-gradient(135deg, var(--portrait-dark) 0%, var(--portrait-light) 55%, #f2f2f2 100%);
  }
  .author-bio {
    position: absolute;
    left: 324px;
    top: 525px;
    width: 194px;
    height: 150px;
    overflow: hidden;
    font-family: "Open Sans", sans-serif;
    font-stretch: 80%;
    font-weight: 400;
    font-size: 12px;
    line-height: 17.5px;
    text-align: justify;
  }

  /* Front cover */
  .front-subtitle {
    position: absolute;
    left: 660px;
    top: 648px;
    width: 512px;
    font-family: "Cinzel", serif;
    font-size: 17.5px;
    line-height: 34px;
    text-align: center;
    text-transform: uppercase;
    white-space: nowrap;
  }
</style>
</head>
<body>
<main class="cover-spread">

  <svg class="graphic-layer" viewBox="0 0 1200 852" aria-hidden="true">
    <!-- Back cover edge title -->
    <text class="ghost-title" transform="translate(-16,6) rotate(90)" textLength="900" lengthAdjust="spacingAndGlyphs">WHERE STORIES BEND SIDEWAYS</text>

    <!-- Spine -->
    <text class="spine-title" transform="translate(581,80) rotate(90)" textLength="555" lengthAdjust="spacingAndGlyphs">WHERE STORIES BEND SIDEWAYS</text>
    <text class="spine-author" transform="translate(581,663) rotate(90)" textLength="152" lengthAdjust="spacingAndGlyphs">DANA MARLOWE</text>

    <!-- Front title -->
    <text class="front-title" x="916" y="128" font-size="62" text-anchor="middle" textLength="450" lengthAdjust="spacingAndGlyphs">WHERE STORIES</text>
    <text class="front-title" x="916" y="284" font-size="178" text-anchor="middle" textLength="488" lengthAdjust="spacingAndGlyphs">BEND</text>
    <text class="front-title" x="916" y="355" font-size="80" text-anchor="middle" textLength="300" lengthAdjust="spacingAndGlyphs">SIDE-</text>
    <text class="front-title" x="916" y="587" font-size="260" text-anchor="middle" textLength="470" lengthAdjust="spacingAndGlyphs">WAYS</text>

    <!-- Front author -->
    <text class="front-author" x="916" y="806" text-anchor="middle" textLength="380" lengthAdjust="spacing">DANA MARLOWE</text>
  </svg>

  <section class="back-cover">
    <h2 class="back-headline">The <em>most</em> important work of art is <em>the</em> life <em>that</em> we create.</h2>
    <p class="back-blurb">In The Maker's Heart, Elias Ray Moreland—author, thought leader, and founder of HARBOR in Portland—pens a manifesto for human creativity and the beginning of a new renais-sance. Moreland not only calls us to reclaim our creative essence but reveals how we can craft our lives into a work of art. There are no shortcuts to quality, and Moreland celebrates the spiritual process that can help us discover our true selves.</p>
    <p class="back-blurb">Moreland demonstrates that we all carry within us the essence of an artist. We all need to create, to be a part of a process that brings to the world something beautiful, good, and true, in order to allow our souls to come to life. It's not only the quality of the ingredients we use to build our lives that matters, but the care we bring to the process itself. Just as with baking artisan bread, it's a process that's crafted over time. And God is the master artisan of our lives. With poignant, inspirational stories and insights from art, life, history, and scripture interspersed throughout, Moreland walks readers through the process of crafting a life of beauty and wonder.</p>
  </section>

  <div class="author-portrait" role="img" aria-label="Black and white portrait photograph of the author"></div>
  <p class="author-bio">Moreland demonstrates that we all carry within us the essence of an artist. We all need to create, to be a part of a process that brings to the world something beautiful, good, and true, in order to allow our souls to come to life. It's not only the quality of the ingredients we use to build our lives that matters, but the care we bring to the p</p>

  <p class="front-subtitle">A Comprehensive Member Experience Guide<br>for Today's Club Management Professional</p>

</main>
</body>
</html>
```